Web Design Project for Web Agency

WHAT I NEED:
The design I need (PSD file) is for a microsite designed for employee recruitment for Brantley, a Web agency.
***Design for the 1st Page ONLY : "Manifeste"
OBJECTIVES OF THE WEBSITE:
1. To promote the agency's corporate culture and HR management principles.
2. To get people to apply on available jobs
ELEMENTS OF THE PAGE "MANIFESTE" :
1. Brantley logo (see attached files). Beside the logo must be the word "Carrières" ("Careers" in english)
***The logo is not final and there is NO branding for Brantley yet. That is why there are multiple files. So please feel free to be creative!
2. Main menu : 4 sections
Manifeste | Opportunités | Brantly | Postuler
3. Manifeste :
This page is the home page. It will present 2 main sections :
a. The agency's corporate culture :
- Title of the page is a question : "Do you embrace Brantley's corporate culture?"
- Then, presentation of the 5 corporate values, each with a title and short description
- At the end of the list of values, we want a button that says "Apply now"
b. The agency's HR management principles :
- Title of the page is a question : "Do you see yourself working at Brantley?"
- Then, presentation of the 5 Management principles, each with a title and short description
- At the end of the list of principles, we want a button that says "Apply now"
VISUAL INSPIRATION
To create each section of the "Manifeste" page, we want a design that will fit with the corporate culture:
- Brantley is BOLD
- Brantley is PROUD
- Brantley is PROFESSIONAL
- Brantley is ELEGANT
- Brantley is REFINED
We want something slick and modern. Here are some Website's that we like that can be of inspiration:
- http://www.studio-vetrak.com/en/services
- http://quorvinpanels.com/

```html
<!DOCTYPE html>
<html lang="en">
<head>
<meta charset="utf-8">
<title>Brantley – Manifeste</title>
<link href="https://fonts.googleapis.com/css2?family=PT+Sans:wght@400;700&family=PT+Sans+Narrow:wght@400;700&display=swap" rel="stylesheet">
<style>
:root{
  --orange:#f47a1f;
  --orange-band:#ff7f12;
  --ink:#1e2833;
  --text:#555;
  --muted:#777;
  --rule:#dcdcdc;
  --footer:#3a3a3a;
  --white:#fff;
}
*{box-sizing:border-box;margin:0;padding:0}
html,body{width:679px;height:1200px;overflow:hidden;background:var(--white)}
body{position:relative;font-family:"PT Sans",sans-serif;color:var(--text)}
.abs{position:absolute}

.brand{left:46px;top:16px}
.brand-name{font-family:"PT Sans",sans-serif;font-weight:700;font-size:33px;color:var(--orange);line-height:1}
.brand-tag{font-size:7.5px;letter-spacing:2.6px;color:#444;margin:4px 0 0 9px}
.main-nav{right:56px;top:35px;display:flex;align-items:center;font-size:12px;color:#555}
.main-nav a{color:inherit;text-decoration:none;padding:0 9px;border-right:1px solid #aaa;line-height:12px}
.social-top{display:flex;gap:4px;margin-left:9px}
.social-top span{width:11px;height:11px;border-radius:50%;background:#666}

.hero{left:0;top:75px;width:679px;height:267px;background:linear-gradient(115deg,#e8f0f8 0%,#b8d2ec 40%,#dbe8f5 65%,#a9c7e6 100%);overflow:hidden}
.hero-globe{left:360px;top:10px;width:190px;height:190px;border-radius:50%;background:radial-gradient(circle at 40% 40%,#cfe1f5,#4f85c7 70%,#2f63a8)}
.hero-title{left:0;width:679px;top:68px;text-align:center;font-family:"PT Sans Narrow",sans-serif;font-weight:700;font-size:35px;color:var(--ink);line-height:1}
.hero-sub{left:0;width:679px;top:107px;text-align:center;font-family:"PT Sans Narrow",sans-serif;font-weight:700;font-size:15px;color:var(--ink)}
.hero-btn{left:267px;top:135px;width:155px;height:27px;background:var(--orange);color:var(--white);font-family:"PT Sans Narrow",sans-serif;font-size:12px;display:flex;align-items:center;justify-content:center;gap:5px}
.hero-arrows{left:610px;top:240px}

.feature{top:362px;width:180px}
.feature h2{font-family:"PT Sans Narrow",sans-serif;font-weight:700;font-size:20px;color:var(--orange);margin-bottom:7px}
.feature p{font-size:7.6px;line-height:12.6px;color:var(--text)}
.feature .more{display:block;margin-top:7px;font-size:7.5px;font-weight:700;color:var(--muted)}

.rule{left:46px;width:590px;height:1px;background:var(--rule)}
.section-title{font-family:"PT Sans Narrow",sans-serif;font-weight:700;font-size:22px;color:var(--ink)}
.section-q{font-family:"PT Sans Narrow",sans-serif;font-size:13.5px;color:var(--orange)}
.point{display:flex;align-items:flex-start;width:270px}
.point .num{flex:none;width:31px;height:31px;border-radius:50%;background:#222;color:var(--white);font-size:14px;display:flex;align-items:center;justify-content:center;margin-right:6px}
.point p{font-size:8.2px;line-height:14px;color:var(--text);padding-top:1px}
.apply{width:72px;height:20px;background:var(--orange);color:var(--white);font-size:8px;display:flex;align-items:center;justify-content:center;border-radius:2px;box-shadow:0 1px 2px rgba(0,0,0,.2)}

.projects{left:0;top:898px;width:679px;height:244px;background:radial-gradient(ellipse at 50% 55%,#ffb060 0%,var(--orange-band) 60%)}
.projects h2{position:absolute;left:45px;top:30px;font-family:"PT Sans Narrow",sans-serif;font-weight:700;font-size:21px;color:var(--white)}
.tile{width:100px;height:100px;border:4px solid var(--white);transform:rotate(45deg);box-shadow:0 2px 6px rgba(0,0,0,.25)}
.caption{color:var(--white);width:100px}
.caption strong{display:block;font-size:9px;font-family:"PT Sans Narrow",sans-serif;font-weight:700}
.caption span{display:block;font-size:6.5px;line-height:9px;opacity:.9}

.footer{left:0;top:1142px;width:679px;height:58px;background:var(--footer)}
.footer p{position:absolute;left:54px;top:19px;font-size:7.5px;color:#bbb}
.social-foot{position:absolute;left:558px;top:16px;display:flex;gap:3px}
.social-foot span{width:16px;height:16px;border-radius:50%;background:var(--white)}
</style>
</head>
<body>

<header>
  <div class="abs brand">
    <div class="brand-name">Brantley</div>
    <div class="brand-tag">AGENCE NUMÉRIQUE</div>
  </div>
  <nav class="abs main-nav">
    <a href="#">Manifeste</a>
    <a href="#">Opportunités</a>
    <a href="#">Brantly</a>
    <a href="#">Postuler</a>
    <div class="social-top"><span></span><span></span><span></span></div>
  </nav>
</header>

<section class="abs hero">
  <div class="abs hero-globe" role="img" aria-label="Desk globe on a soft blue office background"></div>
  <h1 class="abs hero-title">BUSINESS CONSULTANCY</h1>
  <div class="abs hero-sub">ALIQUAM NEC ERAT AT PURUS CURSUS</div>
  <a class="abs hero-btn">VIEW OUR MORE SERVICES
    <svg width="5" height="7" viewBox="0 0 5 7"><path d="M0 0L5 3.5L0 7Z" fill="#fff"/></svg></a>
  <svg class="abs hero-arrows" width="22" height="14" viewBox="0 0 22 14"><path d="M7 1L1 7L7 13M15 1L21 7L15 13" stroke="#222" stroke-width="1.6" fill="none"/></svg>
</section>

<section>
  <div class="abs feature" style="left:52px">
    <h2>Our Technology</h2>
    <p>Phasellus felis dolor, scelerisque a, tempus eget, lobortis id, libero. Donec scelerisque leo ac risus. Praesent sit amet est. In dictum, dolor eu dictum porttitor, enim felis viverra mi</p>
    <span class="more">LEARN MORE</span>
  </div>
  <div class="abs feature" style="left:250px;top:364px">
    <h2>Our Strategy</h2>
    <p>Phasellus felis dolor, scelerisque a, tempus eget, lobortis id, libero. Donec scelerisque leo ac risus. Praesent sit amet est. In dictum, dolor eu dictum porttitor, enim felis viverra mi</p>
    <span class="more">LEARN MORE</span>
  </div>
  <div class="abs feature" style="left:455px;top:364px">
    <h2>Services Provide</h2>
    <p>Phasellus felis dolor, scelerisque a, tempus eget, lobortis id, libero. Donec scelerisque leo ac risus. Praesent sit amet est. In dictum, dolor eu dictum porttitor, enim felis viverra mi</p>
    <span class="more">LEARN MORE</span>
  </div>
</section>

<div class="abs rule" style="top:481px"></div>

<section>
  <h2 class="abs section-title" style="left:46px;top:498px">Corporate Culture</h2>
  <div class="abs section-q" style="left:47px;top:530px">Do you embrace Brantley's corporate culture?</div>
  <div class="abs point" style="left:46px;top:556px"><span class="num">01</span><p>Mauris vel lacus vitae felis vestibulum volutpat. Etiam est nunc, venenatis in, tristique eu, imperdiet ac, nisl.</p></div>
  <div class="abs point" style="left:46px;top:606px"><span class="num">02</span><p>Morbi ornare gravida elit. Integer congue, augue et malesuada iaculis, ipsum dui aliquet felis</p></div>
  <div class="abs point" style="left:354px;top:556px"><span class="num">03</span><p>Suspendisse vulputate aliquam dui. Nulla elementum dui ut augue. Aliquam vehicula mi at mauris</p></div>
  <div class="abs point" style="left:354px;top:606px"><span class="num">04</span><p>Phasellus felis dolor, scelerisque a, tempus eget, lobortis id, libero Donec scelerisque leo ac risus.</p></div>
  <a class="abs apply" style="left:558px;top:651px">APPLY NOW</a>
</section>

<div class="abs rule" style="top:687px"></div>

<section>
  <h2 class="abs section-title" style="left:48px;top:703px">HR management principles</h2>
  <div class="abs section-q" style="left:49px;top:735px">Do you see yourself working at Brantley?</div>
  <div class="abs point" style="left:48px;top:761px"><span class="num">01</span><p>Mauris vel lacus vitae felis vestibulum volutpat. Etiam est nunc, venenatis in, tristique eu, imperdiet ac, nisl.</p></div>
  <div class="abs point" style="left:48px;top:811px"><span class="num">02</span><p>Morbi ornare gravida elit. Integer congue, augue et malesuada iaculis, ipsum dui aliquet felis</p></div>
  <div class="abs point" style="left:356px;top:761px"><span class="num">03</span><p>Suspendisse vulputate aliquam dui. Nulla elementum dui ut augue. Aliquam vehicula mi at mauris</p></div>
  <div class="abs point" style="left:356px;top:811px"><span class="num">04</span><p>Phasellus felis dolor, scelerisque a, tempus eget, lobortis id, libero Donec scelerisque leo ac risus.</p></div>
  <a class="abs apply" style="left:558px;top:861px">APPLY NOW</a>
</section>

<section class="abs projects">
  <h2>Recent Projects</h2>
  <div class="abs tile" style="left:70px;top:86px;background:linear-gradient(135deg,#d9d4cc,#8a8f96)" role="img" aria-label="Business team meeting photo"></div>
  <div class="abs tile" style="left:206px;top:58px;background:linear-gradient(135deg,#6f7e86,#c9c7c0)" role="img" aria-label="Woman reading documents photo"></div>
  <div class="abs tile" style="left:338px;top:84px;background:linear-gradient(135deg,#f0ece6,#2a2a2e)" role="img" aria-label="Group of colleagues photo"></div>
  <div class="abs tile" style="left:475px;top:58px;background:linear-gradient(135deg,#eef0f3,#9aa3ad)" role="img" aria-label="Hands working on a laptop at a desk photo"></div>
  <div class="abs caption" style="left:286px;top:28px"><strong>Suspendisse vul</strong><span>Aliquam dui. Nulla elemen-<br>tum dui ut augue.</span></div>
  <div class="abs caption" style="left:556px;top:28px"><strong>Suspendisse vul</strong><span>Aliquam dui. Nulla elemen-<br>tum dui ut augue.</span></div>
  <div class="abs caption" style="left:153px;top:184px"><strong>Suspendisse vul</strong><span>Aliquam dui. Nulla elemen-<br>tum dui ut augue.</span></div>
  <div class="abs caption" style="left:422px;top:184px"><strong>Suspendisse vul</strong><span>Aliquam dui. Nulla elemen-<br>tum dui ut augue.</span></div>
</section>

<footer class="abs footer">
  <p>© 2013 Company Name.&nbsp; All right reserved.&nbsp; Term of Use</p>
  <div class="social-foot"><span></span><span></span><span></span><span></span></div>
</footer>

</body>
</html>
```